Uprising SaaS company needs an attractive business card design

We're an uprising SaaS company who's attempting to attack the rigid car (insurance) claims management market in Europe.
We want to our mighty base order management system, listen to our clients to connect the smart ideas to build something even mightier.
We primarily focus on helping our customers manage their customers' claims/orders and get them resolved as smoothly as possible.
We'd like the business card design to express technical innovation and the fact that we connect smart ideas, as our company slogan indicates.
Contact Information for Business Card
Name, position, website, email, mobile, business address
Font styles to use
Colors
Designer to choose colors to be used in the design.
Look and feel
Each slider illustrates characteristics of the customer's brand and the style your logo design should communicate.

```html
<!DOCTYPE html>
<html lang="en">
<head>
<meta charset="utf-8">
<title>vantiqo business card</title>
<link rel="stylesheet" href="https://fonts.googleapis.com/css2?family=Montserrat:wght@300;400;700&display=swap">
<style>
  :root {
    --backdrop: #d0d0d0;
    --card-white: #ffffff;
    --card-grey: #7f7f7f;
    --ink-grey: #787878;
    --ink-soft: #8a8a8a;
    --accent-blue: #7ecfe3;
    --ink-white: #ffffff;
  }
  * { box-sizing: border-box; margin: 0; padding: 0; }
  html, body {
    width: 1000px;
    height: 1200px;
    overflow: hidden;
    background: var(--backdrop);
    font-family: "Montserrat", Arial, sans-serif;
  }
  .canvas { position: relative; width: 1000px; height: 1200px; }
  .card {
    position: absolute;
    left: 135px;
    width: 730px;
    height: 417px;
    border-radius: 30px;
    overflow: hidden;
  }
  .card-front { top: 160px; background: var(--card-white); }
  .card-back { top: 623px; background: var(--card-grey); }

  .brand-name {
    position: absolute;
    font-weight: 300;
    letter-spacing: 1px;
    line-height: 1;
    white-space: nowrap;
  }
  .card-front .brand-name {
    left: 55px;
    top: 62px;
    font-size: 76px;
    color: var(--ink-grey);
  }
  .card-back .brand-name {
    left: 0;
    width: 100%;
    top: 148px;
    text-align: center;
    font-size: 112px;
    color: var(--ink-white);
  }

  .person-name {
    position: absolute;
    left: 57px;
    top: 201px;
    font-size: 26px;
    font-weight: 700;
    color: var(--ink-grey);
  }
  .person-role {
    position: absolute;
    left: 57px;
    top: 237px;
    font-size: 18px;
    font-weight: 400;
    color: var(--ink-soft);
  }
  .divider {
    position: absolute;
    left: 57px;
    top: 284px;
    width: 613px;
    height: 2px;
  }
  .contact-list {
    position: absolute;
    left: 58px;
    top: 305px;
    list-style: none;
  }
  .contact-list li {
    display: flex;
    align-items: center;
    height: 25px;
    font-size: 18px;
    color: var(--ink-soft);
  }
  .contact-list svg { width: 16px; height: 16px; margin-right: 12px; flex: none; }
  .address {
    position: absolute;
    left: 513px;
    top: 301px;
    font-style: normal;
    font-size: 18px;
    line-height: 25px;
    color: var(--ink-soft);
  }
</style>
</head>
<body>
<main class="canvas">
  <section class="card card-front" aria-label="Card front">
    <div class="brand-name">vantiqo</div>
    <h1 class="person-name">Daniel Moreau</h1>
    <p class="person-role">Managing Director</p>
    <svg class="divider" viewBox="0 0 613 2" preserveAspectRatio="none" aria-hidden="true">
      <defs>
        <linearGradient id="divider-fade" x1="0" x2="1" y1="0" y2="0">
          <stop offset="0" stop-color="#8a8a8a"/>
          <stop offset="1" stop-color="#7ecfe3"/>
        </linearGradient>
      </defs>
      <line x1="0" y1="1" x2="613" y2="1" stroke="url(#divider-fade)" stroke-width="1.2" stroke-dasharray="4 2"/>
    </svg>
    <ul class="contact-list">
      <li>
        <svg viewBox="0 0 16 16" aria-hidden="true"><path d="M4 2 L6.5 2 L7 5 L5.5 6.3 C6.3 8 7.8 9.6 9.6 10.5 L11 9 L14 9.5 L14 12 C14 13 13 14 12 14 C7 13.5 2.5 9 2 4 C2 3 3 2 4 2Z" fill="#8a8a8a"/></svg>
        1-800-555-0147
      </li>
      <li>
        <svg viewBox="0 0 16 16" aria-hidden="true"><rect x="1.5" y="3.5" width="13" height="9" fill="#8a8a8a"/><path d="M1.5 3.5 L8 9 L14.5 3.5" fill="none" stroke="#fff" stroke-width="1.2"/></svg>
        hello@vantiqo.com
      </li>
      <li>
        <svg viewBox="0 0 16 16" aria-hidden="true"><g fill="none" stroke="#8a8a8a" stroke-width="1.2"><circle cx="8" cy="8" r="6.3"/><ellipse cx="8" cy="8" rx="2.8" ry="6.3"/><line x1="1.7" y1="8" x2="14.3" y2="8"/><line x1="2.8" y1="4.8" x2="13.2" y2="4.8"/><line x1="2.8" y1="11.2" x2="13.2" y2="11.2"/></g></svg>
        www.vantiqo.com
      </li>
    </ul>
    <address class="address">
      4200 Linden Ave<br>
      Maple Grove<br>
      Oregon(OR)
    </address>
  </section>

  <section class="card card-back" aria-label="Card back">
    <div class="brand-name">vantiqo</div>
  </section>
</main>
</body>
</html>
```